Business Cards and label design needed!

I am a metalsmith, working in sterling silver, brass and moving slowly into adding some gold accent pieces. I also use patinas to add color to brass pieces. The peacock feather is used in my packaging, as both a label and tissue paper. I am attaching what I am currently using, and printing at home, but I need a design that I can have professionally printed. My website is www.fernhollowworks.com
Target Market(s)
Established Professionals, Independent thinkers, Art donors, Artist supporters
Industry/Entity Type
Jewelry
Contact Information for Business Card
I would like a business card with the basic contact information, including Facebook and Instagram. I currently use a peacock feather and would like to continue that. I like to use turquoise, Tiffany blue and colors in that direction. I am open to other suggestions. I would like to be able to transfer the design to oval labels as well.
Other font styles liked:
- Garamond or other fonts that have a slight script that is easy to read
Look and feel

```html
<!DOCTYPE html>
<html lang="en">
<head>
<meta charset="UTF-8">
<title>Fern Hollow Works — Business Card</title>
<link href="https://fonts.googleapis.com/css2?family=Playfair+Display:ital,wght@1,400&family=Montserrat:wght@400;700&display=swap" rel="stylesheet">
<style>
  :root {
    --teal: #14a39b;
    --ink: #4a4a4a;
    --rule: #6b6b6b;
    --paper: #ffffff;
    --backdrop: #2b2e33;
    --feather-warm: #c9ab7c;
    --feather-pale: #efe4d2;
  }
  * { margin: 0; padding: 0; box-sizing: border-box; }
  html, body { width: 1200px; height: 1066px; overflow: hidden; }
  body {
    background: var(--backdrop);
    font-family: "Montserrat", sans-serif;
    display: flex;
    flex-direction: column;
    align-items: center;
    justify-content: center;
    gap: 66px;
  }
  .card {
    position: relative;
    width: 700px;
    height: 400px;
    border-radius: 34px;
    overflow: hidden;
    box-shadow: 0 14px 30px rgba(0,0,0,.35);
  }
  .feather-art {
    position: absolute;
    border-radius: 14px;
    background: linear-gradient(135deg, var(--feather-pale), var(--feather-warm));
  }
  .brand {
    font-family: "Playfair Display", serif;
    font-style: italic;
    font-weight: 400;
    color: var(--teal);
    white-space: nowrap;
  }
  /* Front */
  .card-front { background: var(--paper); }
  .card-front .wave { position: absolute; inset: 0; width: 100%; height: 100%; }
  .card-front .feather-art { left: 190px; top: 28px; width: 90px; height: 70px; }
  .card-front .brand { position: absolute; left: 262px; top: 92px; font-size: 44px; }
  .holder {
    position: absolute; left: 300px; top: 176px;
    font-weight: 700; font-size: 30px; color: var(--ink);
  }
  .contact {
    position: absolute; left: 250px; top: 226px;
    list-style: none; font-size: 18px; color: var(--ink);
    display: flex; flex-direction: column; gap: 8px;
  }
  .contact li { display: flex; align-items: center; gap: 10px; }
  .contact li:first-child { padding-left: 40px; }
  .contact svg { width: 16px; height: 16px; flex: none; }
  .website {
    position: absolute; right: 70px; bottom: 18px;
    color: var(--paper); font-size: 20px; letter-spacing: .3px;
  }
  /* Back */
  .card-back { background: var(--teal); }
  .oval {
    position: absolute; left: 120px; top: 60px; width: 460px; height: 280px;
    border-radius: 50%; background: var(--paper);
  }
  .card-back .feather-art { left: 300px; top: 100px; width: 110px; height: 86px; }
  .card-back .brand { position: absolute; left: 0; right: 0; top: 200px; text-align: center; font-size: 40px; }
</style>
</head>
<body>
  <section class="card card-front">
    <svg class="wave" viewBox="0 0 700 400" preserveAspectRatio="none" aria-hidden="true">
      <path d="M0,205 C130,215 210,320 400,338 C520,350 620,340 700,325 L700,400 L0,400Z" fill="var(--rule)"/>
      <path d="M0,216 C130,228 210,332 400,350 C520,362 620,352 700,338 L700,400 L0,400Z" fill="var(--teal)"/>
    </svg>
    <div class="feather-art" role="img" aria-label="Peacock feather illustration"></div>
    <h1 class="brand">Fern Hollow Works</h1>
    <p class="holder">Dana MARLOW</p>
    <ul class="contact">
      <li>
        <svg viewBox="0 0 16 16" aria-hidden="true"><path d="M4 1.5l2.5 3-1.5 1.6c.8 1.8 2.2 3.2 4 4l1.6-1.5 3 2.5-1.6 2.4C7 13 3 9 1.6 3.1Z" fill="var(--teal)"/></svg>
        555.201.3478
      </li>
      <li>
        <svg viewBox="0 0 16 16" aria-hidden="true"><rect x="1" y="3" width="14" height="10" rx="1" fill="none" stroke="var(--teal)" stroke-width="1.6"/><path d="M1.5 3.8 8 9l6.5-5.2" fill="none" stroke="var(--teal)" stroke-width="1.6"/></svg>
        studio@fernhollowworks.com
      </li>
    </ul>
    <p class="website">www.fernhollowworks.com</p>
  </section>

  <section class="card card-back">
    <div class="oval"></div>
    <div class="feather-art" role="img" aria-label="Peacock feather illustration"></div>
    <p class="brand">Fern Hollow Works</p>
  </section>
</body>
</html>
```